Travel video blogger needs website design

I need a website designed for my new travel video blog "Roaming Sparrow". I have only just started but need a website that is fairly simple and not too busy. I have a logo which I want on it (I have attached it to this project). I also want a link to all my other social medias on the main page (vidtrekhub, Snapwell and Palnook) and my videos as well. Here is a link to my vidtrekhub page for you to look at: https://www.vidtrekhub.net/channel/QRm4tZ8pWnE2HX57YKccd31v
As I have only just started and I am still trying to find my specific niche, again I need it to be sleek and simple that I can go in and change slightly here and there. I would like these pages on the website: About Me, Videos, Social Media, Blog, Gallery, contact me. for an example I like the look of www.theroamingkinfolk.net website.

I already have the domain and I am with Harborweb with pagecraftr.org. I just want to spend my time getting better and learning about videos then trying to create a website (I am a bit of a perfectionist when I try to do something).

Target Market(s)

Young Adults (majority females) between the ages of 18 and 30 with an interest in travelling.

Industry/Entity Type

Travel Industry

Number of Pages Required

1 page

Colors

Designer to choose colors to be used in the design.

Requirements
Must have
• A like to my Snapwell, Palnook and vidtrekhub channels on the home page
• Must be a nice, simple design
• Must have my logo on the front and name "Roaming Sparrow"
Nice to have
• A nice light, bright coloured theme
Should not have
• A dark coloured theme

```html
<!DOCTYPE html>
<html lang="en">
<head>
<meta charset="utf-8">
<title>Roaming Sparrow – Travel Video Blog</title>
<link href="https://fonts.googleapis.com/css2?family=Montserrat:wght@400;500;700&family=Playfair+Display:wght@700;900&display=swap" rel="stylesheet">
<style>
  :root {
    --ink: #2b2b2b;
    --muted: #6b6b6b;
    --soft: #8a8a8a;
    --rule: #e3e3e3;
    --accent: #e6a24c;
    --heart: #e5161c;
    --band: #efefef;
    --footer: #2e2e2e;
    --hero-text: rgba(58, 66, 18, 0.88);
    --white: #ffffff;
  }
  * { box-sizing: border-box; margin: 0; padding: 0; }
  html, body { width: 1200px; height: 3169px; overflow: hidden; }
  body {
    position: relative;
    background: var(--white);
    font-family: "Montserrat", Arial, sans-serif;
    color: var(--ink);
  }

  /* Header */
  .site-header { position: absolute; top: 0; left: 0; width: 1200px; height: 125px; border-bottom: 1px solid var(--rule); }
  .brand { position: absolute; top: 30px; left: 0; width: 1200px; display: flex; justify-content: center; align-items: center; gap: 14px; }
  .brand-mark { width: 46px; height: 46px; border: 3px solid var(--ink); border-radius: 50%; }
  .brand-name { font-size: 22px; font-weight: 700; letter-spacing: 2px; text-transform: uppercase; color: var(--ink); }

  .main-nav { position: absolute; top: 125px; left: 0; width: 1200px; height: 52px; display: flex; justify-content: center; align-items: center; gap: 46px; }
  .main-nav a { position: relative; font-size: 13px; font-weight: 500; letter-spacing: 0.6px; color: var(--muted); text-decoration: none; text-transform: uppercase; }
  .main-nav a.is-active { color: var(--accent); }
  .main-nav a.is-active::before { content: ""; position: absolute; left: -4px; right: -4px; top: -20px; height: 2px; background: var(--accent); }

  /* Hero */
  .hero { position: absolute; top: 177px; left: 0; width: 1200px; height: 552px;
    background: linear-gradient(180deg, #e9e3cf 0%, #efe1b8 22%, #c7cf96 45%, #9fb766 70%, #b6c48c 100%); }
  .hero-title { position: absolute; top: 190px; left: 0; width: 1200px; text-align: center;
    font-family: "Playfair Display", Georgia, serif; font-weight: 900; font-size: 98px; line-height: 112px;
    letter-spacing: 2px; text-transform: uppercase; color: var(--hero-text); }

  /* Posts grid */
  .posts { position: absolute; top: 824px; left: 78px; width: 1044px; display: flex; justify-content: space-between; }
  .post-column { width: 332px; display: flex; flex-direction: column; }
  .post { margin-bottom: 42px; }
  .post-photo { width: 332px; }
  .post-photo.tall { height: 353px; }
  .post-photo.short { height: 247px; }
  .post-meta { margin-top: 20px; height: 24px; display: flex; align-items: center; font-size: 12px; color: var(--muted); }
  .post-date { display: flex; align-items: center; gap: 8px; }
  .post-likes { margin-left: auto; display: flex; align-items: center; gap: 8px; }
  .post-share { margin-left: 18px; display: flex; align-items: center; }
  .post-excerpt { margin-top: 13px; font-size: 12.5px; line-height: 25px; color: var(--muted); }

  /* Follow strip */
  .follow-band { position: absolute; top: 2688px; left: 0; width: 1200px; height: 97px; background: var(--band); }
  .follow-strip { position: absolute; top: 2785px; left: 0; width: 1200px; height: 218px; display: flex; }
  .follow-strip .strip-photo { flex: 1; height: 218px; }
  .follow-button { position: absolute; top: 2876px; left: 539px; width: 123px; height: 42px; border-radius: 4px;
    background: rgba(30, 30, 30, 0.78); color: var(--white); font-size: 14px; display: flex; align-items: center; justify-content: center; gap: 8px; }
  .follow-button .dot { width: 12px; height: 12px; border: 1.5px solid var(--white); border-radius: 3px; }

  .social-links { position: absolute; top: 3038px; left: 0; width: 1200px; display: flex; justify-content: center; gap: 46px; }
  .social-links a { display: flex; align-items: center; gap: 10px; font-size: 14px; color: var(--muted); text-decoration: none; }
  .social-links .dot { width: 14px; height: 14px; border-radius: 50%; background: var(--soft); }

  .site-footer { position: absolute; top: 3106px; left: 0; width: 1200px; height: 63px; background: var(--footer);
    color: #d8d8d8; font-size: 13px; display: flex; align-items: center; justify-content: center; letter-spacing: 0.3px; }

  /* Photo placeholders */
  .ph-bali { background: linear-gradient(180deg, #1e7fd0 0%, #8cc3e8 40%, #3e7d4a 68%, #55a7b8 100%); }
  .ph-coast { background: linear-gradient(180deg, #6ea6d8 0%, #b9d3e6 30%, #caa570 55%, #3fb0b4 80%, #e6d2ae 100%); }
  .ph-river { background: linear-gradient(180deg, #3f6b2e 0%, #6b8a3a 45%, #a48a5a 75%, #d9c9a6 100%); }
  .ph-city-dusk { background: linear-gradient(180deg, #5d7bb0 0%, #a9b4d0 40%, #d9a25a 60%, #2f4f86 100%); }
  .ph-family-road { background: linear-gradient(180deg, #8fb8dc 0%, #dce7ee 45%, #7e8b8f 72%, #5d6266 100%); }
  .ph-cliff { background: linear-gradient(180deg, #9aa6b0 0%, #c7cdd1 40%, #6b705a 70%, #8d7a66 100%); }
  .ph-sunhat { background: linear-gradient(180deg, #b9d4ea 0%, #7ea3c2 45%, #e2cfa4 65%, #d4342a 100%); }
  .ph-pier { background: linear-gradient(180deg, #8fc5e8 0%, #3ea0cf 45%, #c9a78d 75%, #a8705a 100%); }
  .ph-statue { background: linear-gradient(180deg, #9cc4e6 0%, #cfdde6 30%, #5f7b6a 60%, #6fa53c 100%); }
  .ph-canal { background: linear-gradient(180deg, #5b97d6 0%, #dfe7ee 35%, #b69a7a 55%, #2fa0a6 100%); }
  .ph-sunset { background: linear-gradient(180deg, #f0c258 0%, #f5e1a8 40%, #d8a26a 70%, #f1e6dc 100%); }
  .ph-tower { background: linear-gradient(180deg, #3d64a8 0%, #8da6cf 45%, #c9a3a0 70%, #6b6e5a 100%); }
  .ph-strip-city { background: linear-gradient(180deg, #7d92c0 0%, #d7a865 55%, #2f4f86 100%); }
  .ph-strip-coast { background: linear-gradient(180deg, #8ab2d6 0%, #caa570 50%, #3fb0b4 100%); }
  .ph-strip-sunset { background: linear-gradient(180deg, #f0b35a 0%, #d2705a 55%, #5a3d3a 100%); }
  .ph-strip-aurora { background: linear-gradient(180deg, #0e2a4a 0%, #1f8a7a 40%, #2a4d7a 70%, #dfe7ef 100%); }
</style>
</head>
<body>

<header class="site-header">
  <div class="brand">
    <span class="brand-mark"></span>
    <span class="brand-name">Roaming Sparrow</span>
  </div>
</header>

<nav class="main-nav">
  <a href="#" class="is-active">Home</a>
  <a href="#">About Me</a>
  <a href="#">Videos</a>
  <a href="#">Social Media</a>
  <a href="#">Blog</a>
  <a href="#">Gallery</a>
  <a href="#">Contact Me</a>
</nav>

<section class="hero" role="img" aria-label="Aerial view of green highland hills with a winding road and a lake at sunrise">
  <h1 class="hero-title">Lets Explore<br>The World</h1>
</section>

<svg width="0" height="0" style="position:absolute">
  <defs>
    <symbol id="icon-calendar" viewBox="0 0 16 16">
      <rect x="1.5" y="3" width="13" height="11.5" rx="1" fill="none" stroke="#2b2b2b" stroke-width="1.6"/>
      <rect x="1.5" y="3" width="13" height="3" fill="#2b2b2b"/>
      <line x1="4.5" y1="1" x2="4.5" y2="4" stroke="#2b2b2b" stroke-width="1.6"/>
      <line x1="11.5" y1="1" x2="11.5" y2="4" stroke="#2b2b2b" stroke-width="1.6"/>
      <g fill="#2b2b2b"><rect x="4" y="8" width="2" height="2"/><rect x="7" y="8" width="2" height="2"/><rect x="10" y="8" width="2" height="2"/><rect x="4" y="11" width="2" height="2"/><rect x="7" y="11" width="2" height="2"/></g>
    </symbol>
    <symbol id="icon-heart" viewBox="0 0 20 18">
      <path d="M10 17.5 L2 9.5 C-0.5 7 0.2 2.2 4 1.2 C6.5 0.6 8.6 1.8 10 3.8 C11.4 1.8 13.5 0.6 16 1.2 C19.8 2.2 20.5 7 18 9.5 Z" fill="#e5161c"/>
    </symbol>
    <symbol id="icon-share" viewBox="0 0 22 16">
      <path d="M13 1 L21 7.5 L13 14 L13 10 C7 10 3.5 11.5 1 15 C2 9 5.5 5.5 13 5 Z" fill="#1e1e1e"/>
    </symbol>
  </defs>
</svg>

<main class="posts">
  <div class="post-column">
    <article class="post">
      <div class="post-photo tall ph-bali" role="img" aria-label="Tiered lake temple with mountains and blue sky"></div>
      <div class="post-meta"><span class="post-date"><svg width="16" height="16"><use href="#icon-calendar"/></svg>12 FEB 2018</span><span class="post-likes"><svg width="20" height="18"><use href="#icon-heart"/></svg>266</span><span class="post-share"><svg width="22" height="16"><use href="#icon-share"/></svg></span></div>
      <p class="post-excerpt">Lorem Ipsum is simply dummy text of the printing and typesetting industry Lorem Ipsum.</p>
    </article>
    <article class="post">
      <div class="post-photo short ph-city-dusk" role="img" aria-label="Riverside parliament building and chain bridge lit at dusk"></div>
      <div class="post-meta"><span class="post-date"><svg width="16" height="16"><use href="#icon-calendar"/></svg>12 FEB 2018</span><span class="post-likes"><svg width="20" height="18"><use href="#icon-heart"/></svg>266</span><span class="post-share"><svg width="22" height="16"><use href="#icon-share"/></svg></span></div>
      <p class="post-excerpt">Lorem Ipsum is simply dummy text of the printing and typesetting industry Lorem Ipsum.</p>
    </article>
    <article class="post">
      <div class="post-photo tall ph-sunhat" role="img" aria-label="Traveller in a wide sun hat looking out over a sea bay"></div>
      <div class="post-meta"><span class="post-date"><svg width="16" height="16"><use href="#icon-calendar"/></svg>12 FEB 2018</span><span class="post-likes"><svg width="20" height="18"><use href="#icon-heart"/></svg>266</span><span class="post-share"><svg width="22" height="16"><use href="#icon-share"/></svg></span></div>
      <p class="post-excerpt">Lorem Ipsum is simply dummy text of the printing and typesetting industry Lorem Ipsum.</p>
    </article>
    <article class="post">
      <div class="post-photo short ph-canal" role="img" aria-label="Gondola on a canal in front of a domed basilica"></div>
      <div class="post-meta"><span class="post-date"><svg width="16" height="16"><use href="#icon-calendar"/></svg>12 FEB 2018</span><span class="post-likes"><svg width="20" height="18"><use href="#icon-heart"/></svg>266</span><span class="post-share"><svg width="22" height="16"><use href="#icon-share"/></svg></span></div>
      <p class="post-excerpt">Lorem Ipsum is simply dummy text of the printing and typesetting industry Lorem Ipsum.</p>
    </article>
  </div>

  <div class="post-column">
    <article class="post">
      <div class="post-photo short ph-coast" role="img" aria-label="Limestone sea stacks along a turquoise coastline"></div>
      <div class="post-meta"><span class="post-date"><svg width="16" height="16"><use href="#icon-calendar"/></svg>12 FEB 2018</span><span class="post-likes"><svg width="20" height="18"><use href="#icon-heart"/></svg>266</span><span class="post-share"><svg width="22" height="16"><use href="#icon-share"/></svg></span></div>
      <p class="post-excerpt">Lorem Ipsum is simply dummy text of the printing and typesetting industry Lorem Ipsum.</p>
    </article>
    <article class="post">
      <div class="post-photo tall ph-family-road" role="img" aria-label="Parent helping a small child ride a balance bike on a lakeside road"></div>
      <div class="post-meta"><span class="post-date"><svg width="16" height="16"><use href="#icon-calendar"/></svg>12 FEB 2018</span><span class="post-likes"><svg width="20" height="18"><use href="#icon-heart"/></svg>266</span><span class="post-share"><svg width="22" height="16"><use href="#icon-share"/></svg></span></div>
      <p class="post-excerpt">Lorem Ipsum is simply dummy text of the printing and typesetting industry Lorem Ipsum.</p>
    </article>
    <article class="post">
      <div class="post-photo short ph-pier" role="img" aria-label="Family with luggage walking along a pier by the sea"></div>
      <div class="post-meta"><span class="post-date"><svg width="16" height="16"><use href="#icon-calendar"/></svg>12 FEB 2018</span><span class="post-likes"><svg width="20" height="18"><use href="#icon-heart"/></svg>266</span><span class="post-share"><svg width="22" height="16"><use href="#icon-share"/></svg></span></div>
      <p class="post-excerpt">Lorem Ipsum is simply dummy text of the printing and typesetting industry Lorem Ipsum.</p>
    </article>
    <article class="post">
      <div class="post-photo tall ph-sunset" role="img" aria-label="Couple sitting together on a deck watching a golden sunset"></div>
      <div class="post-meta"><span class="post-date"><svg width="16" height="16"><use href="#icon-calendar"/></svg>12 FEB 2018</span><span class="post-likes"><svg width="20" height="18"><use href="#icon-heart"/></svg>266</span><span class="post-share"><svg width="22" height="16"><use href="#icon-share"/></svg></span></div>
      <p class="post-excerpt">Lorem Ipsum is simply dummy text of the printing and typesetting industry Lorem Ipsum.</p>
    </article>
  </div>

  <div class="post-column">
    <article class="post">
      <div class="post-photo tall ph-river" role="img" aria-label="Wooden boat travelling down a palm-lined river"></div>
      <div class="post-meta"><span class="post-date"><svg width="16" height="16"><use href="#icon-calendar"/></svg>12 FEB 2018</span><span class="post-likes"><svg width="20" height="18"><use href="#icon-heart"/></svg>266</span><span class="post-share"><svg width="22" height="16"><use href="#icon-share"/></svg></span></div>
      <p class="post-excerpt">Lorem Ipsum is simply dummy text of the printing and typesetting industry Lorem Ipsum.</p>
    </article>
    <article class="post">
      <div class="post-photo short ph-cliff" role="img" aria-label="Monastery perched on a rock pillar above a misty valley"></div>
      <div class="post-meta"><span class="post-date"><svg width="16" height="16"><use href="#icon-calendar"/></svg>12 FEB 2018</span><span class="post-likes"><svg width="20" height="18"><use href="#icon-heart"/></svg>266</span><span class="post-share"><svg width="22" height="16"><use href="#icon-share"/></svg></span></div>
      <p class="post-excerpt">Lorem Ipsum is simply dummy text of the printing and typesetting industry Lorem Ipsum.</p>
    </article>
    <article class="post">
      <div class="post-photo tall ph-statue" role="img" aria-label="Stone statue in a garden overlooking a mountain lake"></div>
      <div class="post-meta"><span class="post-date"><svg width="16" height="16"><use href="#icon-calendar"/></svg>12 FEB 2018</span><span class="post-likes"><svg width="20" height="18"><use href="#icon-heart"/></svg>266</span><span class="post-share"><svg width="22" height="16"><use href="#icon-share"/></svg></span></div>
      <p class="post-excerpt">Lorem Ipsum is simply dummy text of the printing and typesetting industry Lorem Ipsum.</p>
    </article>
    <article class="post">
      <div class="post-photo short ph-tower" role="img" aria-label="Old clock tower between palm trees with birds in flight"></div>
      <div class="post-meta"><span class="post-date"><svg width="16" height="16"><use href="#icon-calendar"/></svg>12 FEB 2018</span><span class="post-likes"><svg width="20" height="18"><use href="#icon-heart"/></svg>266</span><span class="post-share"><svg width="22" height="16"><use href="#icon-share"/></svg></span></div>
      <p class="post-excerpt">Lorem Ipsum is simply dummy text of the printing and typesetting industry Lorem Ipsum.</p>
    </article>
  </div>
</main>

<div class="follow-band"></div>
<section class="follow-strip">
  <div class="strip-photo ph-strip-city" role="img" aria-label="Riverside city skyline with bridge at dusk"></div>
  <div class="strip-photo ph-strip-coast" role="img" aria-label="Sea stacks on a turquoise coast"></div>
  <div class="strip-photo ph-strip-sunset" role="img" aria-label="Traveller photographing a mountain sunset"></div>
  <div class="strip-photo ph-strip-aurora" role="img" aria-label="Northern lights over snowy mountains"></div>
</section>
<a class="follow-button" href="#"><span class="dot"></span>Follow us</a>

<nav class="social-links">
  <a href="#"><span class="dot"></span>Snapwell</a>
  <a href="https://www.vidtrekhub.net/channel/QRm4tZ8pWnE2HX57YKccd31v"><span class="dot"></span>Vidtrekhub</a>
  <a href="#"><span class="dot"></span>Palnook</a>
</nav>

<footer class="site-footer">2018 ©ROAMING SPARROW – All Rights Reserved.</footer>

</body>
</html>
```